Ridgeview Helping Neighbors Gate Fold Brochure

I would like a color, double sided, gate folded brochure based off of 8.5"x11" paper.I have attached a word file with information that I would like contained within the brochure. The logo that I was told to use for this brochure is attached, but it is of low quality. Please do with it what you can, and we would prefer the color blue instead of purple, if at all possible. The logo would go on the front of the brochure, along with the text"Ridgeview Helping Neighbors" & "Because We Care...", just without the quotes.The only other item that we would like in a certain spot, is a card that could be cut out of the back side of the brochure and mailed in with a donation. On it, we would like lines for someone to write their Name, Address, City, State, Zip Code, Phone, E-mail Address. AT the bottom of the card, we would like it to say "Please mail card and donation payable to Ridgeview Helping Neighbors, PO Box 518, Brindale, OH 44872".Our facebook page is called Ridgeview Helping Neighbors (https://www.examplesocial.test/Ridgeview-Helping-Neighbors-493017265810447/), and you can find various photos there to use on the brochure. There are pictures from a bingo contest, outdoor cookout, and bake sale, and would like a picture (or more) used from each within the brochure.

Colors

Designer to choose colors to be used in the design.

Requirements
Must have
• I need a brochure that uses a gate fold.

```html
<!DOCTYPE html>
<html lang="en">
<head>
<meta charset="utf-8">
<title>Ridgeview Helping Neighbors – Gate Fold Brochure Inside Spread</title>
<link href="https://fonts.googleapis.com/css2?family=Open+Sans:wght@400;600;700&display=swap" rel="stylesheet">
<style>
  :root {
    --page-bg: #e9e9e6;
    --paper-light: #f6f6f6;
    --paper-mid: #dcdcdc;
    --navy: #0f3563;
    --deep-navy: #0b2a55;
    --ocean: #1a6fb0;
    --sky: #2c9fd6;
    --teal: #2aa3b8;
    --headline: #2a9fd8;
    --text: #16396b;
    --photo-frame: #ffffff;
  }
  * { box-sizing: border-box; margin: 0; padding: 0; }
  html, body { width: 1200px; height: 900px; overflow: hidden; }
  body {
    background: var(--page-bg);
    font-family: "Open Sans", Arial, sans-serif;
    color: var(--text);
  }
  .brochure {
    position: absolute;
    left: 50px; top: 25px;
    width: 1100px; height: 850px;
    background: linear-gradient(160deg, var(--paper-light) 0%, #ececec 55%, var(--paper-mid) 100%);
    box-shadow: 0 10px 30px rgba(0,0,0,.25);
    overflow: hidden;
  }
  .brochure__art { position: absolute; inset: 0; width: 100%; height: 100%; }
  .fold {
    position: absolute; top: 0; bottom: 0; width: 2px;
    background: linear-gradient(90deg, rgba(0,0,0,.07), rgba(255,255,255,.5));
  }
  .fold--left { left: 275px; }
  .fold--right { left: 825px; }

  .headline {
    position: absolute; left: 120px; top: 60px;
    color: var(--headline);
    font-weight: 600; font-size: 24px; letter-spacing: 1px;
    line-height: 1.35; text-transform: uppercase;
    white-space: nowrap;
  }
  .headline__second { display: block; padding-left: 22px; }

  .photo {
    position: absolute;
    border: 6px solid var(--photo-frame);
    box-shadow: 0 4px 12px rgba(0,0,0,.35);
  }
  .photo--volunteers { left: 470px; top: 160px; width: 200px; height: 130px; background: linear-gradient(135deg, #6b4a34, #9aa5ae 60%, #c9c9c4); }
  .photo--cookout { left: 770px; top: 150px; width: 190px; height: 125px; background: linear-gradient(135deg, #7c8a7d, #c8c9c2 45%, #5d6a58); }
  .photo--bingo { left: 190px; top: 360px; width: 200px; height: 130px; background: linear-gradient(135deg, #d7d3c8, #8a7d74 50%, #6d4a48); }
  .photo--bakesale { left: 440px; top: 340px; width: 200px; height: 128px; background: linear-gradient(135deg, #c9c0a8, #b58a6b 50%, #c24b24); }
  .photo--parade { left: 780px; top: 430px; width: 195px; height: 125px; background: linear-gradient(135deg, #8a8f86, #a3343a 50%, #3b3f4a); }

  .section { position: absolute; font-size: 14px; line-height: 1.38; }
  .section__title { font-weight: 700; font-size: 16px; text-transform: uppercase; color: var(--deep-navy); }
  .section--who { left: 130px; top: 195px; width: 310px; }
  .section--purpose { left: 700px; top: 305px; width: 290px; }
  .section--funds { left: 330px; top: 515px; width: 420px; }
  .section--apply { left: 370px; top: 628px; width: 440px; }

  .tagline {
    position: absolute; left: 555px; top: 750px;
    display: flex; align-items: center; gap: 16px;
  }
  .tagline__mark { width: 76px; height: 76px; background: var(--ocean); }
  .tagline__text {
    font-size: 24px; font-weight: 400; color: var(--ocean);
    letter-spacing: 3px; line-height: 1.2;
  }
</style>
</head>
<body>
  <main class="brochure" aria-label="Gate fold brochure inside spread">
    <svg class="brochure__art" viewBox="0 0 1100 850" aria-hidden="true">
      <path d="M0 300 C 80 520, 260 760, 560 850 L 0 850 Z" fill="var(--navy)"/>
      <path d="M0 330 C 110 560, 300 770, 600 850 L 560 850 C 260 760, 80 540, 0 360 Z" fill="var(--ocean)"/>
      <path d="M60 310 C 150 560, 340 760, 700 850 L 640 850 C 330 770, 140 560, 40 330 Z" fill="var(--sky)" opacity=".85"/>
      <path d="M0 450 C 120 650, 330 800, 520 850 L 0 850 Z" fill="var(--deep-navy)"/>
      <path d="M1100 200 C 990 300, 980 520, 1040 850 L 1100 850 Z" fill="var(--ocean)"/>
      <path d="M1100 170 C 960 260, 960 520, 1010 850 L 1040 850 C 985 520, 990 300, 1100 200 Z" fill="var(--teal)" opacity=".55"/>
    </svg>
    <div class="fold fold--left"></div>
    <div class="fold fold--right"></div>

    <h1 class="headline">A new 501(c)3 non-profit group for helping families
      <span class="headline__second">with medical or catastrophic events .</span></h1>

    <div class="photo photo--volunteers" role="img" aria-label="Photo of two volunteers standing together in a kitchen"></div>
    <div class="photo photo--cookout" role="img" aria-label="Photo of the outdoor cookout under a tent"></div>
    <div class="photo photo--bingo" role="img" aria-label="Photo of a crowded hall during the bingo fundraiser"></div>
    <div class="photo photo--bakesale" role="img" aria-label="Photo of baskets and baked goods on a bake sale table"></div>
    <div class="photo photo--parade" role="img" aria-label="Photo of children riding a decorated cart in a holiday parade"></div>

    <section class="section section--who">
      <p><span class="section__title">Who are we:</span> A group of experienced fundraisers who wish to assist Ridgeview County residents with medical needs. We formed Ridgeview Helping Neighbors to provide a service to the county.</p>
    </section>
    <section class="section section--purpose">
      <p><span class="section__title">What is our purpose:</span> To provide short-term charitable assistance to Ridgeview County residents with out-of-pocket expenses incurred due to illness or catastrophic events.</p>
    </section>
    <section class="section section--funds">
      <p><span class="section__title">Where do our funds come from?</span> The organization conducts fundraisers and accepts donations. We are 501(c)3 tax exempt, so all donations are tax deductible. We are also planning to apply for any applicable grants that might be available. All donations are appreciated.</p>
    </section>
    <section class="section section--apply">
      <p><span class="section__title">How do people apply for assistance:</span> Applications are available at Valleycrest Medical Center from Dana Whitfield and at the Harmony Center at the Fairgrounds. Residents can also contact any member of the board to give information and help to someone in need.</p>
    </section>

    <div class="tagline">
      <span class="tagline__mark" aria-hidden="true"></span>
      <p class="tagline__text">Because<br>We Care</p>
    </div>
  </main>
</body>
</html>
```